Business cards for start-up accounting firm

I'm looking for a double sided business card ready for upload into Prontel ink or similar print providers with no modification required by me.
I'm looking for something simple as i think cards that are too 'busy' actually detract from the message. I have some thoughts but more than happy to see what comes up. The logo i have came out of left field and i love it the moment i saw it!

My thoughts:

Side 1: Just the logo, perhaps on a dark grey or charcoal background to make the logo colours stand out?

Side 2: The call to action from me website 'Looking for a more relaxed, friendly and interactive relationship with your accountant?' with my contact information
Name: Gavin Ormsby
Email: gavin@quellorix.com.au
Website: www.quellorix.com.au
Phone: 1300 742 916

The call to action needs to be the first thing they see when they look at side 2. If it helps to know what we do and how we do it there is a draft website at www.quellorix.com.au

Like i said, happy to consider anything that comes up :)

Target Market(s)

i'm targeting small business owners who experience a lot of stress around finacial reporting and have had bad experiences with accountants in the past.

Industry/Entity Type

Accounting

Contact Information for Business Card

Contained in the Description

Font styles to use
Serif
Sans Serif
Other font styles liked:
• See logo files attached

Colors
474747

Requirements
Must have
• My logo, slogan and contact information

```html
<!DOCTYPE html>
<html lang="en">
<head>
<meta charset="utf-8">
<title>Quellorix — Business Cards</title>
<link rel="stylesheet" href="https://fonts.googleapis.com/css2?family=Exo+2:wght@700&family=Montserrat:wght@400;600&display=swap">
<style>
  :root {
    --backdrop: #ececec;
    --yellow: #fdd400;
    --purple: #8b3375;
    --charcoal: #333333;
    --white: #ffffff;
    --lavender: #c9a3cf;
  }
  * { margin: 0; padding: 0; box-sizing: border-box; }
  html, body { width: 1200px; height: 985px; overflow: hidden; }
  body {
    background: var(--backdrop);
    position: relative;
    font-family: "Montserrat", sans-serif;
  }
  .card { position: absolute; overflow: hidden; }
  .card-shapes { position: absolute; inset: 0; display: block; }
  .card--front { left: 217px; top: 148px; width: 583px; height: 333px; }
  .card--back  { left: 473px; top: 519px; width: 585px; height: 336px; }

  .brand-name {
    position: absolute;
    font-family: "Exo 2", sans-serif;
    font-weight: 700;
    color: var(--yellow);
    line-height: 1;
    letter-spacing: 1px;
    text-align: center;
    white-space: nowrap;
  }
  .brand-slogan {
    position: absolute;
    display: flex; align-items: center; justify-content: center; gap: 8px;
    color: var(--lavender);
    text-transform: uppercase;
    letter-spacing: 1.6px;
    white-space: nowrap;
    line-height: 1;
  }
  .brand-slogan::before, .brand-slogan::after {
    content: ""; flex: 1; height: 1px; background: var(--lavender);
  }
  .card--front .brand-name { left: 241px; width: 322px; top: 130px; font-size: 58px; }
  .card--front .brand-slogan { left: 241px; width: 322px; top: 225px; font-size: 12.5px; }
  .card--back .brand-name { left: 382px; width: 154px; top: 130px; font-size: 28px; }
  .card--back .brand-slogan { left: 382px; width: 154px; top: 175px; font-size: 6px; gap: 4px; letter-spacing: 0.8px; }

  .call-to-action {
    position: absolute; left: 8px; top: 18px; width: 330px;
    color: var(--white); font-size: 13.5px; line-height: 19px; text-align: center;
  }
  .contact-name {
    position: absolute; left: 27px; top: 100px; width: 218px;
    padding-bottom: 6px;
    border-bottom: 2px solid var(--white);
    font-family: "Exo 2", sans-serif; font-weight: 700;
    font-size: 25px; color: var(--white); text-align: center; letter-spacing: 0.5px;
  }
  .contact-item {
    position: absolute; left: 10px; width: 240px;
    color: var(--white); text-align: center;
  }
  .contact-value { font-weight: 600; font-size: 16.5px; line-height: 20px; }
  .contact-label { font-size: 15px; line-height: 20px; }
  .contact-item--email { top: 168px; }
  .contact-item--web { top: 226px; }
  .contact-phone {
    position: absolute; left: 20px; top: 290px;
    color: var(--white); font-weight: 600; font-size: 21px; letter-spacing: 0.3px;
  }
</style>
</head>
<body>

<section class="card card--front" aria-label="Business card front">
  <svg class="card-shapes" viewBox="0 0 583 333" preserveAspectRatio="none" aria-hidden="true">
    <rect width="583" height="333" fill="var(--yellow)"/>
    <path d="M323 0 C230 40 150 160 125 333 L583 333 L583 0 Z" fill="var(--purple)" stroke="var(--white)" stroke-width="1.5"/>
    <path d="M338 0 C240 40 180 140 205 230 C215 270 235 310 255 333 L583 333 L583 0 Z" fill="var(--charcoal)" stroke="var(--white)" stroke-width="1.5"/>
    <rect x="0" y="318" width="126" height="6" fill="var(--purple)"/>
    <rect x="126" y="318" width="457" height="6" fill="var(--yellow)"/>
    <rect x="0" y="324" width="126" height="9" fill="var(--yellow)"/>
    <line x1="126" y1="318" x2="126" y2="333" stroke="var(--white)" stroke-width="1.5"/>
  </svg>
  <div class="brand-name">QUELLORIX</div>
  <div class="brand-slogan">Calm books, clear growth</div>
</section>

<section class="card card--back" aria-label="Business card back">
  <svg class="card-shapes" viewBox="0 0 585 336" preserveAspectRatio="none" aria-hidden="true">
    <rect width="585" height="336" fill="var(--purple)"/>
    <path d="M407 0 C300 40 250 150 268 230 C276 270 290 310 302 336 L585 336 L585 0 Z" fill="var(--yellow)" stroke="var(--white)" stroke-width="1.5"/>
    <path d="M432 0 C330 40 290 150 310 230 C322 275 350 315 385 336 L585 336 L585 0 Z" fill="var(--charcoal)" stroke="var(--white)" stroke-width="1.5"/>
    <rect x="0" y="320" width="300" height="6" fill="var(--yellow)"/>
    <rect x="300" y="318" width="285" height="6" fill="var(--purple)"/>
  </svg>
  <p class="call-to-action">Looking for a more relaxed, friendly and interactive relationship with your accountant?</p>
  <h1 class="contact-name">Gavin Ormsby</h1>
  <div class="contact-item contact-item--email">
    <div class="contact-value">gavin@quellorix.com.au</div>
    <div class="contact-label">Email:</div>
  </div>
  <div class="contact-item contact-item--web">
    <div class="contact-value">www.quellorix.com.au</div>
    <div class="contact-label">Website:</div>
  </div>
  <div class="contact-phone">Phone: 1300 742 916</div>
  <div class="brand-name">QUELLORIX</div>
  <div class="brand-slogan">Calm books, clear growth</div>
</section>

</body>
</html>
```